Property management company looking for modern card design

We at Blue Maple Holdings provides property management services for its residential and commercial properties, with expertise in all categories of multifamily, industrial and office projects throughout California.

We need a business card design that is professional and modern designed business card. In our field, clients get hundreds of business cards, we would like our card to stand out.

Please avoid small print.

Target Market(s)

Professionals and high end clients

Industry/Entity Type

Financial Planning

Contact Information for Business Card

Company Name: Blue Maple Holdings, Name, email, license #, phone number, website bluemapleholdings.example

Font styles to use
Sans Serif

Requirements
Must have
• The card design needs to be adaptable because there is a possibly we will be expanding into different sectors other than real estate. The card design should be focused on financial planning and asset management.
Nice to have
• Modern and simple business card. Eye catching. Non-standard size/shaped cards would be great.
• bluemapleholdings.example
Should not have
• Too many bright color or any pictures or shapes of real estate stuff.

```html
<!DOCTYPE html>
<html lang="en">
<head>
<meta charset="utf-8">
<title>Blue Maple Holdings – Business Card</title>
<link rel="stylesheet" href="https://fonts.googleapis.com/css2?family=Raleway:wght@500;600&family=Open+Sans:wght@400&display=swap">
<style>
  :root {
    --page-bg: #e9e7e3;
    --card-white: #fbfbfb;
    --card-black: #141414;
    --brand-red: #e0262b;
    --ink: #2a2a2a;
    --ink-soft: #555555;
    --shadow: rgba(0, 0, 0, 0.22);
  }
  * { margin: 0; padding: 0; box-sizing: border-box; }
  html, body {
    width: 771px;
    height: 1200px;
    overflow: hidden;
    background: var(--page-bg);
  }
  .canvas {
    position: relative;
    width: 771px;
    height: 1200px;
  }
  .card {
    position: absolute;
    left: 66px;
    width: 640px;
    height: 366px;
    border-radius: 18px;
    box-shadow: 0 10px 26px var(--shadow);
    overflow: hidden;
  }
  .card--front { top: 140px; background: var(--card-white); }
  .card--back  { top: 680px; background: var(--card-black); }

  .brand {
    position: absolute;
    display: flex;
    align-items: center;
    gap: 16px;
    font-family: "Raleway", sans-serif;
    font-weight: 500;
    font-size: 34px;
    letter-spacing: 0.5px;
    color: var(--brand-red);
    white-space: nowrap;
  }
  .brand__dot {
    width: 46px;
    height: 46px;
    border-radius: 50%;
    background: var(--brand-red);
    flex: none;
  }
  .card--front .brand { top: 76px; right: 52px; }
  .card--back .brand { top: 50%; left: 50%; transform: translate(-50%, -50%); }

  .holder {
    position: absolute;
    left: 40px;
    bottom: 58px;
    padding-left: 16px;
    border-left: 5px solid var(--brand-red);
  }
  .holder__name {
    font-family: "Raleway", sans-serif;
    font-weight: 600;
    font-size: 30px;
    color: var(--ink);
    line-height: 1.1;
  }
  .holder__title {
    font-family: "Raleway", sans-serif;
    font-weight: 500;
    font-size: 17px;
    color: var(--brand-red);
    margin-top: 4px;
  }

  .contact {
    position: absolute;
    right: 44px;
    bottom: 36px;
    list-style: none;
    font-family: "Open Sans", sans-serif;
    font-size: 15px;
    color: var(--ink-soft);
  }
  .contact__item {
    display: flex;
    align-items: center;
    gap: 10px;
    line-height: 28px;
    white-space: nowrap;
  }
  .contact__icon { width: 15px; height: 15px; flex: none; }
</style>
</head>
<body>
<main class="canvas">

  <section class="card card--front" aria-label="Business card front">
    <div class="brand"><span class="brand__dot"></span>Blue Maple Holdings</div>

    <div class="holder">
      <p class="holder__name">Your Name</p>
      <p class="holder__title">Job Title</p>
    </div>

    <ul class="contact">
      <li class="contact__item">
        <svg class="contact__icon" viewBox="0 0 16 16" aria-hidden="true">
          <path d="M2 5c0-2 2-3 6-3s6 1 6 3v1h-3V5H5v1H2z" fill="#e0262b"/>
          <rect x="3" y="8" width="10" height="6" rx="1.5" fill="#e0262b"/>
          <circle cx="8" cy="11" r="1.6" fill="#fbfbfb"/>
        </svg>
        000 000 0000
      </li>
      <li class="contact__item">
        <svg class="contact__icon" viewBox="0 0 16 16" aria-hidden="true">
          <rect x="1" y="3" width="14" height="10" rx="1.5" fill="#e0262b"/>
          <path d="M1.5 4l6.5 5 6.5-5" fill="none" stroke="#fbfbfb" stroke-width="1.3"/>
        </svg>
        youremail@mailbox.example
      </li>
      <li class="contact__item">
        <svg class="contact__icon" viewBox="0 0 16 16" aria-hidden="true">
          <circle cx="8" cy="8" r="6.5" fill="none" stroke="#e0262b" stroke-width="1.4"/>
          <ellipse cx="8" cy="8" rx="2.8" ry="6.5" fill="none" stroke="#e0262b" stroke-width="1.1"/>
          <path d="M1.5 8h13" stroke="#e0262b" stroke-width="1.1"/>
        </svg>
        www.bluemapleholdings.example
      </li>
      <li class="contact__item">
        <svg class="contact__icon" viewBox="0 0 16 16" aria-hidden="true">
          <rect x="2" y="1.5" width="12" height="13" rx="1.5" fill="#e0262b"/>
          <path d="M5 5.5h6M5 8h6M5 10.5h4" stroke="#fbfbfb" stroke-width="1.2"/>
        </svg>
        License # 00000000
      </li>
    </ul>
  </section>

  <section class="card card--back" aria-label="Business card back">
    <div class="brand"><span class="brand__dot"></span>Blue Maple Holdings</div>
  </section>

</main>
</body>
</html>
```